Ridgeline Builders Guild Business card

We are looking for a new business card design with photo included.
Our business is a nonprofit construction contractor membership organization. We offer business education, assist with business setup and licensing, provide safety training, and provide a member directory.
URL: www.ridgelinebuildersguild.org
Color code:
CMYK: 0 cyan, 42 magenta, 100 yellow, 0 black for Print.
Hexidecimal: #FF9900
RGB: R 255; G 153; B 0

```html
<!DOCTYPE html>
<html lang="en">
<head>
<meta charset="utf-8">
<title>Ridgeline Builders Guild – Business Card</title>
<link rel="stylesheet" href="https://fonts.googleapis.com/css2?family=Arimo:wght@400;700&display=swap">
<style>
  :root {
    --orange: #FF9900;
    --ink: #2a2a2a;
    --muted: #3c3c3c;
    --paper: #f7f7f7;
    --night: #222324;
    --stage: #e4e4e4;
    --rule: #8a8a8a;
  }
  * { box-sizing: border-box; margin: 0; padding: 0; }
  html, body { width: 1200px; height: 930px; overflow: hidden; }
  body {
    background: var(--stage);
    font-family: "Arimo", Arial, sans-serif;
    color: var(--ink);
    position: relative;
  }
  .card {
    position: absolute;
    left: 250px;
    width: 700px;
    height: 400px;
    box-shadow: 0 4px 14px rgba(0,0,0,0.12);
  }
  .card--front { top: 60px; background: var(--paper); }
  .card--back  { top: 490px; background: var(--night); }

  /* front */
  .holder { position: absolute; left: 48px; top: 52px; }
  .holder__name {
    color: var(--orange);
    font-weight: 700;
    font-size: 25px;
    letter-spacing: 0.5px;
    text-transform: uppercase;
  }
  .holder__title {
    font-size: 15px;
    letter-spacing: 0.6px;
    text-transform: uppercase;
    margin-top: 4px;
    color: var(--muted);
  }
  .contacts { list-style: none; margin-top: 18px; }
  .contacts li {
    display: flex;
    align-items: center;
    gap: 10px;
    font-size: 17px;
    line-height: 26px;
    color: var(--muted);
  }
  .contacts svg { width: 18px; height: 18px; flex: none; }
  .divider {
    position: absolute;
    left: 300px;
    right: 0;
    top: 232px;
    height: 1px;
    background: var(--rule);
  }
  .wordmark {
    position: absolute;
    right: 44px;
    top: 70px;
    text-align: right;
    font-weight: 700;
    font-size: 40px;
    line-height: 44px;
    color: var(--ink);
    text-transform: uppercase;
    letter-spacing: -0.5px;
  }
  .address {
    position: absolute;
    right: 48px;
    bottom: 44px;
    text-align: right;
    font-size: 18px;
    line-height: 24px;
    color: var(--muted);
  }

  /* back */
  .back-mark {
    position: absolute;
    left: 50%;
    top: 120px;
    transform: translateX(-50%);
    display: flex;
    align-items: center;
    gap: 16px;
    white-space: nowrap;
  }
  .back-mark__dot {
    width: 34px; height: 34px; border-radius: 50%;
    background: var(--orange);
  }
  .back-mark__name {
    font-weight: 700;
    font-size: 30px;
    color: #ffffff;
    text-transform: uppercase;
  }
  .back-url {
    position: absolute;
    left: 0; right: 0;
    bottom: 70px;
    text-align: center;
    font-size: 16px;
    letter-spacing: 1px;
    color: #ffffff;
    text-transform: uppercase;
  }
  .back-url span { color: var(--orange); }
</style>
</head>
<body>

<section class="card card--front" aria-label="Business card front">
  <div class="holder">
    <h1 class="holder__name">Daniel Whitaker</h1>
    <p class="holder__title">Managing Director</p>
    <ul class="contacts">
      <li>
        <svg viewBox="0 0 18 18" aria-hidden="true"><circle cx="9" cy="9" r="9" fill="var(--orange)"/><path d="M6 5 l2 0 l1 2.5 l-1.2 1 a5 5 0 0 0 2.2 2.2 l1-1.2 l2.5 1 l0 2 a1 1 0 0 1 -1 1 A8 8 0 0 1 5 6 a1 1 0 0 1 1 -1z" fill="#fff"/></svg>
        (555) 201-3380 (Office)
      </li>
      <li>
        <svg viewBox="0 0 18 18" aria-hidden="true"><circle cx="9" cy="9" r="9" fill="var(--orange)"/><rect x="5" y="5.5" width="8" height="7" rx="1" fill="none" stroke="#fff" stroke-width="1.4"/></svg>
        800-555-0142
      </li>
      <li>
        <svg viewBox="0 0 18 18" aria-hidden="true"><circle cx="9" cy="9" r="9" fill="var(--orange)"/><rect x="6.5" y="4" width="5" height="10" rx="1" fill="#fff"/></svg>
        555.318.0427
      </li>
      <li>
        <svg viewBox="0 0 18 18" aria-hidden="true"><circle cx="9" cy="9" r="9" fill="var(--orange)"/><rect x="4.5" y="6" width="9" height="6.5" fill="#fff"/><path d="M4.5 6 L9 9.6 L13.5 6" fill="none" stroke="var(--orange)" stroke-width="1"/></svg>
        support@rbguild.org
      </li>
      <li>
        <svg viewBox="0 0 18 18" aria-hidden="true"><circle cx="9" cy="9" r="9" fill="var(--orange)"/><circle cx="9" cy="9" r="4.5" fill="none" stroke="#fff" stroke-width="1.3"/><path d="M4.5 9 H13.5 M9 4.5 V13.5" stroke="#fff" stroke-width="1.1"/></svg>
        www.ridgelinebuildersguild.org
      </li>
    </ul>
  </div>

  <div class="wordmark">Ridgeline<br>Builders Guild</div>
  <div class="divider"></div>

  <address class="address" style="font-style:normal">
    2400 NW Alder Way<br>
    Suite #210, Ashford<br>
    OR 97000
  </address>
</section>

<section class="card card--back" aria-label="Business card back">
  <div class="back-mark">
    <span class="back-mark__dot"></span>
    <span class="back-mark__name">Ridgeline Builders Guild</span>
  </div>
  <p class="back-url">www.<span>ridgelinebuildersguild</span>.org</p>
</section>

</body>
</html>
```